Quillstone Restaurnt Lunch Menu Redesign:

We have two lunch special menus that need to be reformatted into a 4.25inx11in and need a graphics design update. Some menu items need to change and some descriptions need to updated. This new menu should double sided with the Main Dining Lunch Menu on the front side and Teppanyaki Lunch menu on the back.

Both menus should follow the same design formatting as the main dining lunch menu (font, sizing, ect.)

```html
<!DOCTYPE html>
<html lang="en">
<head>
<meta charset="utf-8">
<title>Quillstone Restaurant Lunch Menu</title>
<link rel="stylesheet" href="https://fonts.googleapis.com/css2?family=Libre+Baskerville:ital,wght@0,400;0,700;1,400&display=swap">
<style>
  :root {
    --backdrop: #efefef;
    --paper: #ffffff;
    --ink: #111111;
    --ink-soft: #2a2a2a;
    --rule-soft: #e2e2e2;
  }
  * { margin: 0; padding: 0; box-sizing: border-box; }
  html, body { width: 1128px; height: 1200px; overflow: hidden; }
  body {
    background: var(--backdrop);
    font-family: "Libre Baskerville", Georgia, serif;
    color: var(--ink);
    position: relative;
  }
  .menu-side {
    position: absolute;
    top: 21px;
    width: 449px;
    height: 1158px;
    background: var(--paper);
  }
  .menu-side--front { left: 96px; }
  .menu-side--back { left: 584px; }
  .block { position: absolute; left: 0; right: 0; text-align: center; }

  .brand-line {
    font-size: 38px;
    line-height: 44px;
    letter-spacing: 1px;
    font-weight: 400;
    text-transform: uppercase;
  }
  .brand-line--top { top: 28px; }
  .brand-line--bottom { top: 76px; }

  .menu-title { font-size: 39px; line-height: 44px; font-weight: 700; }
  .section-title { font-size: 27px; line-height: 32px; font-weight: 700; }
  .subtitle { font-size: 17px; line-height: 20px; font-style: italic; }
  .note { font-size: 11.5px; line-height: 16px; font-style: italic; color: var(--ink-soft); }

  .sandwich-list { left: 22px; right: 32px; top: 308px; text-align: left; }
  .sandwich {
    height: 35px;
    display: flex;
    justify-content: space-between;
    align-items: center;
  }
  .sandwich-name { font-size: 12.5px; line-height: 17px; font-weight: 700; }
  .sandwich-desc { display: block; font-size: 12px; line-height: 17px; font-style: italic; font-weight: 400; padding-left: 10px; }
  .price { font-size: 14.5px; }

  .sushi-grid {
    left: 22px; right: 12px; top: 550px;
    display: grid;
    grid-template-columns: 235px 1fr;
    grid-auto-rows: 25.4px;
    text-align: left;
    font-size: 12.5px;
    align-items: center;
  }
  .sushi-grid b { font-weight: 700; }
  .sushi-grid i { font-style: italic; }

  .course-list { left: 22px; right: 32px; top: 827px; text-align: left; }
  .course {
    height: 25.6px;
    display: flex;
    justify-content: space-between;
    align-items: center;
    font-size: 12.5px;
  }
  .course b { font-weight: 700; }
  .course i { font-style: italic; }

  .price-list { left: 23px; right: 23px; text-align: left; }
  .price-row {
    display: flex;
    justify-content: space-between;
    align-items: center;
    font-size: 13.5px;
    color: var(--ink-soft);
  }
  .price-list--teppanyaki { top: 273px; }
  .price-list--teppanyaki .price-row { height: 28.3px; }
  .price-list--special { top: 864px; }
  .price-list--special .price-row { height: 27px; }
  .price-row span:last-child { font-size: 14.5px; color: var(--ink); }

  .sunrise {
    position: absolute;
    left: 149px;
    width: 150px;
    height: 40px;
    top: 1044px;
    background: linear-gradient(to top, var(--rule-soft), rgba(255,255,255,0));
    border-bottom: 1px solid var(--rule-soft);
  }
  .raw-key { font-size: 14px; line-height: 16px; }
  .fine-print { font-size: 10.5px; line-height: 14px; }
  .fine-print--small { font-size: 9.5px; line-height: 13px; }
</style>
</head>
<body>

<section class="menu-side menu-side--front">
  <div class="block brand-line brand-line--top">Quillstone</div>
  <div class="block brand-line brand-line--bottom">Restaurant</div>

  <h1 class="block menu-title" style="top:157px">Lunch Specials</h1>
  <p class="block subtitle" style="top:205px">Served Daily 11AM - 3PM</p>

  <h2 class="block section-title" style="top:247px">Sandwiches</h2>
  <p class="block note" style="top:287px">Served with Choice of Miso Soup or House Salad &amp; Potato Chips</p>
  <div class="block sandwich-list">
    <div class="sandwich"><div class="sandwich-name">Fried Breaded Calamari Steak<span class="sandwich-desc">with Tomato, Lettuce &amp; Onion</span></div><span class="price">$16</span></div>
    <div class="sandwich"><div class="sandwich-name">Grilled Chicken<span class="sandwich-desc">with Bacon, Tomato, Lettuce &amp; Mayonnaise Drizzle</span></div><span class="price">$16</span></div>
    <div class="sandwich"><div class="sandwich-name">Hamburger<span class="sandwich-desc">with Lettuce, Tomato, Onion, Mayonnaise Drizzle</span></div><span class="price">$18</span></div>
    <div class="sandwich"><div class="sandwich-name">Fried Soft Shell Crab Burger<span class="sandwich-desc">with Avocado, Lettuce, Tomato, Onion &amp; Mayo</span></div><span class="price">$20</span></div>
  </div>

  <h2 class="block section-title" style="top:468px">Sushi Specials</h2>
  <p class="block note" style="top:507px">Please Select 4 of the followings for $ 16</p>
  <p class="block note" style="top:532px">Served with a 4 piece California Roll &amp; Miso Soup or House Salad</p>
  <div class="block sushi-grid">
    <div><b>*Hamachi</b> - <i>Yellowtail Tuna</i></div><div><b>*Maguro</b> - <i>Yellow fin Tuna</i></div>
    <div><b>*Hotate</b> - <i>Scallop</i></div><div><b>*Smoked Salmon</b></div>
    <div><b>*Ika</b> - <i>Squid</i></div><div></div>
    <div><b>*Ikura</b> - <i>Salmon Roe</i></div><div><b>Tako</b> - <i>Octopus</i></div>
    <div><b>*Saba</b> - <i>Mackerel</i></div><div><b>Unagi</b> - <i>BBQ Eel</i></div>
    <div><b>*Sake</b> - <i>Salmon</i></div><div><b>Ebi</b> - <i>Shrimp</i></div>
    <div><b>*Tai</b> - <i>Red Snapper</i></div><div><b>Tamago</b> - <i>Egg</i></div>
  </div>

  <h2 class="block section-title" style="top:743px">Main Courses</h2>
  <p class="block note" style="top:782px">Served with Rice &amp; Choice of Miso Soup or House Salad</p>
  <p class="block note" style="top:807px">All Meals Served with Rice.&nbsp; Upgrade to fried rice for only $4</p>
  <div class="block course-list">
    <div class="course"><span><b>Organic Tofu Teriyaki</b> - <i>Served Grilled or Tempura Fried</i></span><span class="price">$14</span></div>
    <div class="course"><b>Chicken Teriyaki</b><span class="price">$16</span></div>
    <div class="course"><b>Spicy Chicken Teriyaki</b><span class="price">$16</span></div>
    <div class="course"><b>Beef Teriyaki</b><span class="price">$16</span></div>
    <div class="course"><b>Spicy Beef Teriyaki</b><span class="price">$16</span></div>
    <div class="course"><span><b>Chicken Katsu</b> - <i>Breaded Chicken Breast</i></span><span class="price">$15</span></div>
    <div class="course"><span><b>Katsu Don</b> - <i>Fried Chicken Breast, Egg &amp; Onion over Rice</i></span><span class="price">$16</span></div>
    <div class="course"><span><b>Unagi Don</b> - <i>BBQ Eel over Rice</i></span><span class="price">$19</span></div>
    <div class="course"><b>Shrimp &amp; Vegetable Tempura</b><span class="price">$16</span></div>
  </div>

  <div class="sunrise" role="img" aria-label="Faint sunrise line ornament"></div>
  <p class="block raw-key" style="top:1087px">*Served Raw</p>
  <p class="block fine-print" style="top:1111px">20% gratuity added to parties of 6 or more.</p>
  <p class="block fine-print fine-print--small" style="top:1129px">Consuming raw or undercooked food may increase your risk of foodborne illness</p>
</section>

<section class="menu-side menu-side--back">
  <div class="block brand-line brand-line--top">Quillstone</div>
  <div class="block brand-line brand-line--bottom">Restaurant</div>

  <h2 class="block section-title" style="top:161px">Teppanyaki Lunch</h2>
  <p class="block subtitle" style="top:205px">Available until 11AM - 2:30PM</p>
  <p class="block note" style="top:234px">Served with Miso Soup or Salad, Choice of Rice &amp; Vegetables</p>
  <div class="block price-list price-list--teppanyaki">
    <div class="price-row"><span style="color:var(--ink)">Hibachi Chicken</span><span>$ 18.00</span></div>
    <div class="price-row"><span>Hibachi Shrimp</span><span>$ 19.00</span></div>
    <div class="price-row"><span>Hibachi New York Steak</span><span>$ 20.00</span></div>
    <div class="price-row"><span>Hibachi Salmon</span><span>$ 20.00</span></div>
    <div class="price-row"><span>Teriyaki Beef</span><span>$ 19.00</span></div>
    <div class="price-row"><span>Hibachi Scallop</span><span>$ 20.00</span></div>
    <div class="price-row"><span>Chicken and Shrimp</span><span>$ 21.00</span></div>
    <div class="price-row"><span>Scallop and Shrimp</span><span>$ 22.00</span></div>
    <div class="price-row"><span>New York Steak and Chicken</span><span>$ 22.00</span></div>
    <div class="price-row"><span>New York Steak and Shrimp</span><span>$ 23.00</span></div>
    <div class="price-row"><span>New York Steak and Scallop</span><span>$ 24.00</span></div>
    <div class="price-row"><span>Filet Mignon</span><span>$ 23.00</span></div>
    <div class="price-row"><span>Filet Mignon and Chicken</span><span>$ 25.00</span></div>
    <div class="price-row"><span>Filet Mignon and Shrimp</span><span>$ 26.00</span></div>
    <div class="price-row"><span>Filet Mignon and Scallop</span><span>$ 27.00</span></div>
  </div>

  <h2 class="block menu-title" style="top:741px">Special Menu</h2>
  <p class="block subtitle" style="top:792px">Ages 12 and Under ~ Ages 65 and Older</p>
  <p class="block note" style="top:826px">Served with Miso Soup or Salad, Choice of Rice &amp; Vegetables</p>
  <div class="block price-list price-list--special">
    <div class="price-row"><span>Hibachi Chicken</span><span>$ 15.00</span></div>
    <div class="price-row"><span>Hibachi Shrimp</span><span>$ 16.00</span></div>
    <div class="price-row"><span>Hibachi Scallop</span><span>$ 18.00</span></div>
    <div class="price-row"><span>Hibachi New York Steak</span><span>$ 18.00</span></div>
    <div class="price-row"><span>Hibachi Scallop</span><span>$ 18.00</span></div>
    <div class="price-row"><span>Teriyaki Beef</span><span>$ 16.00</span></div>
  </div>

  <div class="sunrise" role="img" aria-label="Faint sunrise line ornament"></div>
  <p class="block fine-print" style="top:1111px">20% gratuity added to parties of 6 or more.</p>
  <p class="block fine-print fine-print--small" style="top:1129px">Consuming raw or undercooked food may increase your risk of foodborne illness</p>
</section>

</body>
</html>
```